Occasions chocolate packaging

We are looking for 7 packaging designs for bars of chocolate.

Each design needs to be different and we’re not looking for a consistent brand or branding message across the designs. Inspiration should come from gift/occasion cards. Fun, simple, bold, vibrant colours and eye catching, i.e. not vintage or just text.

The front of the packaging should have the main message on and is free of any branding. You don’t need to design the back, just simply allow the main background colour or design pattern to continue around.

These are the different designs we are after, I’ve added in some text for each to give you some guidance but feel free to play around with the message if it suits the design better.

1) Mum
‘The best mum’, ‘Best mum in the World’, ‘Number 1 Mum’

2) Dad
‘The Best Dad’, ‘Best Dad Ever’, ‘Number 1 Dad’, ‘You’re my hero Dad’

3) Husband
‘Best Husband in the World’, ‘Husband I Love You’, ‘Darling Husband’

4) Wife
‘Best Wife in the World’, ‘For my Wonderful Wife’, ‘My Beautiful Wife’

5) Congratulations
Simple one, just Congratulations

6) Thinking of you
Try and keep this neutral as it could be used for happy and sad situations.

7) Thank you
Keep this gender neutral.

Sides:
The sides need to have the following text:

FINE BELGIAN DARK CHOCOLATE
infused with Orange

Back:
The main colour of the front should continue all the way around, we will place a box with the contents and bar code on here ourselves so no need to do anything.

Dimensions:
Attached in the document, front of package is 85mm by 190mm.

The packaging is made from folded card, the first blank part is for gluing the back on to.

Reason: I'm extending the deadline as I've only received 1 design so far which has followed the brief. Although I do like it, I would like to see at least some competition...

```html
<!DOCTYPE html>
<html lang="en">
<head>
<meta charset="UTF-8">
<title>Wife Chocolate Bar Wrapper</title>
<link href="https://fonts.googleapis.com/css2?family=Lobster&family=Baloo+2:wght@600&display=swap" rel="stylesheet">
<style>
  :root {
    --page-bg: #ffffff;
    --wrapper-base: #5b4a44;
    --choc-dark: #3b2219;
    --choc-mid: #6b4131;
    --choc-light: #8a5a44;
    --skin-shadow: #6f6661;
    --skin-mid: #9c8f89;
    --skin-light: #b7aaa3;
    --pink: #ea4fee;
    --pink-light: #f19af2;
    --outline: #ffffff;
    --shadow: rgba(60, 30, 60, 0.55);
    --text-light: #ffffff;
  }
  * { margin: 0; padding: 0; box-sizing: border-box; }
  html, body {
    width: 1200px;
    height: 598px;
    overflow: hidden;
    background: var(--page-bg);
  }
  .canvas {
    position: relative;
    width: 1200px;
    height: 598px;
  }
  .wrapper-front {
    position: absolute;
    left: 60px;
    top: 48px;
    width: 1080px;
    height: 500px;
    overflow: hidden;
    background: var(--wrapper-base);
  }
  .chocolate-photo {
    position: absolute;
    left: 0;
    top: 0;
    width: 600px;
    height: 100%;
    background:
      radial-gradient(ellipse 260px 320px at 230px 210px, var(--choc-light), transparent 70%),
      linear-gradient(110deg, var(--choc-dark) 0%, var(--choc-mid) 45%, var(--choc-dark) 80%, rgba(59,34,25,0) 100%);
  }
  .portrait-photo {
    position: absolute;
    right: 0;
    top: 0;
    width: 600px;
    height: 100%;
    background:
      radial-gradient(ellipse 280px 300px at 360px 230px, var(--skin-light), transparent 75%),
      linear-gradient(90deg, rgba(111,102,97,0) 0%, var(--skin-shadow) 25%, var(--skin-mid) 70%, var(--skin-shadow) 100%);
  }
  .title,
  .title-outline {
    position: absolute;
    left: 0;
    width: 100%;
    top: 96px;
    text-align: center;
    font-family: "Lobster", cursive;
    font-size: 196px;
    letter-spacing: 8px;
    line-height: 1;
  }
  .title {
    background: linear-gradient(180deg, var(--pink) 35%, var(--pink-light) 80%);
    -webkit-background-clip: text;
    background-clip: text;
    -webkit-text-fill-color: transparent;
  }
  .title-outline {
    color: var(--outline);
    -webkit-text-stroke: 14px var(--outline);
    text-shadow: 5px 7px 8px var(--shadow);
  }
  .weight-badge {
    position: absolute;
    left: 178px;
    top: 276px;
    width: 130px;
    height: 130px;
  }
  .weight-badge-label {
    position: absolute;
    left: 178px;
    top: 276px;
    width: 130px;
    height: 130px;
    display: flex;
    align-items: center;
    justify-content: center;
    font-family: "Lobster", cursive;
    font-size: 27px;
    color: var(--text-light);
  }
  .subtitle {
    position: absolute;
    left: 332px;
    top: 318px;
    font-family: "Baloo 2", sans-serif;
    font-weight: 600;
    font-size: 52px;
    line-height: 1.2;
    color: var(--text-light);
    text-shadow: 2px 3px 4px rgba(0,0,0,0.35);
    white-space: nowrap;
  }
</style>
</head>
<body>
  <main class="canvas">
    <section class="wrapper-front">
      <div class="chocolate-photo" role="img" aria-label="Photo of broken milk chocolate bar pieces and shavings"></div>
      <div class="portrait-photo" role="img" aria-label="Soft close-up portrait photo of a smiling woman"></div>

      <h1 class="title-outline" aria-hidden="true">Wife</h1>
      <h1 class="title">Wife</h1>

      <svg class="weight-badge" viewBox="0 0 140 140" aria-hidden="true">
        <defs>
          <linearGradient id="badgeFill" x1="0" y1="0" x2="0" y2="1">
            <stop offset="0" stop-color="#f39bf3"/>
            <stop offset="1" stop-color="#ea4fee"/>
          </linearGradient>
        </defs>
        <path fill="url(#badgeFill)" d="M70 6 Q84 4 94 12 Q110 10 116 24 Q132 30 130 46 Q140 58 134 72 Q140 86 130 96 Q130 112 116 116 Q108 130 94 128 Q82 138 70 134 Q58 138 46 128 Q30 130 24 116 Q10 112 10 96 Q0 86 6 72 Q0 58 10 46 Q8 30 24 24 Q30 10 46 12 Q56 4 70 6 Z"/>
      </svg>
      <div class="weight-badge-label">20grams</div>

      <p class="subtitle">For my Wonderful Wife</p>
    </section>
  </main>
</body>
</html>
```